Organic skincare label - minimalist, earthy, luxe design needed!

I need a label design for a luxury natural skin care line called "Velka Botanix". Velka means 'earth' in Swahili. I would like the design to embody an earthy feel but be minimalistic and give a luxe vibe. My first product will be a Tumeric and Neem Scrub.

The size of the jar is 8oz, label dimensions should be (1.625" Tall x 8.5" Wide)
I will be making other products too such as; oils + toners so I feel free to do labels for glass bottles and/or spray bottles as well.

Forest green, light pinks/nudes/beige, grey, white, gold, are colors that can be used (not all have to be used).

I have included pictures of some things I've worked on myself as well as my original logo design but I need to simplify the logo, no circle around it.
Feel free to get creative.

Thank you! :)
Updates

Target Market(s)

Socially Conscious, Beauty Enthusiast, Minimalist

Industry/Entity Type

Skin Care

Font styles to use
Sans Serif
Other font styles liked:
• "Wonderlove doodle" is the font used for "Velka" in the logo. Feel free to use that or change it as you see fit.

Requirements
Must have
• Simplistic design
would like to stick to a font close to the ones in the logo. Either the one used for the name "Velka" OR the one that the slogan "ROOTED RITUALS" uses.

I have also included some pictures to capture the aesthetic of my social media and website.

Gender neutral

```html
<!DOCTYPE html>
<html lang="en">
<head>
<meta charset="utf-8">
<title>Velka Botanix – Tumeric and Neem Scrub Label</title>
<link href="https://fonts.googleapis.com/css2?family=Poppins:wght@400;500;600&display=swap" rel="stylesheet">
<style>
  :root {
    --page-bg: #efefef;
    --label-green: #21250f;
    --copper: #b97c52;
    --peach: #e3ab88;
    --white: #ffffff;
  }
  html, body {
    margin: 0;
    padding: 0;
    width: 1200px;
    height: 1200px;
    overflow: hidden;
    background: radial-gradient(ellipse at 50% 40%, #f6f6f6 0%, var(--page-bg) 70%, #e6e6e6 100%);
    font-family: "Poppins", sans-serif;
  }
  .label {
    position: absolute;
    left: 75px;
    top: 500px;
    width: 1050px;
    height: 200px;
    background: var(--label-green);
  }
  .brand {
    position: absolute;
    left: 0;
    right: 0;
    top: 38px;
    text-align: center;
    color: var(--copper);
    font-weight: 600;
    font-size: 48px;
    line-height: 60px;
    letter-spacing: 1px;
  }
  .tagline {
    position: absolute;
    left: 0;
    right: 0;
    top: 102px;
    text-align: center;
    color: var(--copper);
    font-weight: 500;
    font-size: 10.5px;
    line-height: 14px;
    letter-spacing: 0.6px;
  }
  .product-name {
    position: absolute;
    left: 0;
    right: 0;
    top: 131px;
    margin: 0;
    text-align: center;
    color: var(--white);
    font-weight: 400;
    font-size: 19px;
    line-height: 28px;
  }
  .volume {
    position: absolute;
    left: 0;
    right: 0;
    top: 173px;
    text-align: center;
    color: var(--peach);
    font-size: 7.5px;
    line-height: 11px;
  }
  .ingredients {
    position: absolute;
    right: 22px;
    top: 112px;
    margin: 0;
    text-align: right;
    color: var(--peach);
    font-size: 7.8px;
    line-height: 13.8px;
  }
  .origin {
    position: absolute;
    right: 22px;
    top: 174px;
    margin: 0;
    color: var(--peach);
    font-weight: 600;
    font-size: 7.8px;
    line-height: 11px;
  }
</style>
</head>
<body>
  <section class="label" aria-label="Velka Botanix jar label">
    <div class="brand">Velka</div>
    <div class="tagline">ROOTED RITUALS</div>
    <h1 class="product-name">Tumeric and Neem Scrub</h1>
    <div class="volume">8oz / 59ml</div>
    <p class="ingredients">Ingredients Organic Rosehip<br>Seed Oil, Organic Camelia Seed<br>Oil, Organic Pomegranate<br>Oil, VitaminE non-GMO</p>
    <p class="origin">MADE IN HOUSTON, TX</p>
  </section>
</body>
</html>
```